Consulting Website

We are looking at renewing out company's website. we are an organizational development consulting firm that works within the Middle East and Africa. Our focus on on organizations within the Gulf area.

We are looking to having a simple, clean and attractive website. pictures should be relevant to our location.

We are also looking for a creative design, something that isn't just "another consulting website"
Updates

Thank you all for submitting your designs, following are some general comments;

- Having a veiled women on the intro is NOT a must
- have a picture with people is NOT a must too, we can use nature, symbols, places..anything really!
- Here are some sites i like;
brightwaveteams.example
http://www.harborlanehomes.example/
http://www.quillterrace.example/
http://www.verdano.example/

I hope these could give you some idea :)

thanks again.

Industry/Entity Type

It Company

Requirements
Must have
• Tabs for press, testimonials, products, resources and services.
pictures also should be relevant to the geographical location. i.e. veiled women, men in traditional costumes and so on.

It's very important that we MAINTAIN the corporate colors of the logo.
Should not have
• Clean and neat design!
i REALLY dont like crowded designs.

```html
<!DOCTYPE html>
<html lang="en">
<head>
<meta charset="utf-8">
<title>TELOS Consulting</title>
<link rel="stylesheet" href="https://fonts.googleapis.com/css2?family=Arimo:wght@400;700&family=Open+Sans:wght@400;600&display=swap">
<style>
:root{
  --slate:#5e7384;
  --slate-dark:#465968;
  --slate-light:#8096a7;
  --nav-dark:#2d3135;
  --nav-mid:#44484c;
  --ink:#3c3c3c;
  --heading:#2f4150;
  --accent:#4a6478;
  --panel-bg:#ffffff;
  --page-bg:#ffffff;
  --hero-bg:#eef0f2;
  --line:#c9d0d6;
  --red-link:#b0212b;
  --white:#ffffff;
}
*{margin:0;padding:0;box-sizing:border-box}
html,body{width:750px;height:1200px;overflow:hidden;background:var(--page-bg)}
body{position:relative;font-family:"Open Sans",Verdana,sans-serif;color:var(--ink)}
.abs{position:absolute}

/* header */
.brand{left:30px;top:20px;display:flex;align-items:center;gap:10px}
.brand-mark{width:50px;height:50px;background:var(--slate-light)}
.brand-name{font-family:"Arimo",Arial,sans-serif;font-size:30px;color:var(--slate);letter-spacing:1px;white-space:nowrap}
.search{left:570px;top:20px;width:142px;height:24px;border-radius:4px;background:linear-gradient(#8095a6,#667b8c);box-shadow:inset 0 1px 2px rgba(0,0,0,.3)}
.search svg{position:absolute;right:6px;top:3px}
.phone{left:562px;top:55px;display:flex;align-items:center;gap:8px;font-family:"Arimo",Arial,sans-serif;font-size:18px;color:#222;white-space:nowrap}
.phone-icon{width:20px;height:22px;border-radius:3px;background:var(--slate-light);display:flex;align-items:center;justify-content:center}

/* navigation */
.nav-band{left:0;top:90px;width:750px;height:50px;background:linear-gradient(var(--slate),var(--slate-dark))}
.nav{left:30px;top:96px;width:692px;height:38px;border-radius:4px;background:linear-gradient(var(--nav-mid),var(--nav-dark));display:flex;align-items:center;padding-left:11px}
.nav a{font-family:"Arimo",Arial,sans-serif;font-size:11px;color:var(--white);text-decoration:none;height:38px;line-height:38px;padding:0 23px;border-right:1px solid #8a9096;white-space:nowrap}
.nav a:last-child{border-right:none}
.nav a.current{background:#55595d;height:30px;line-height:30px;padding:0 17px;border-radius:3px;border-right:none;margin-right:12px}

/* hero */
.hero-band{left:0;top:140px;width:750px;height:262px;background:var(--hero-bg);border-bottom:1px solid #dde1e4}
.hero{left:30px;top:150px;width:692px;height:245px;border:1px solid #b7bcc0;border-radius:4px;overflow:hidden;background:linear-gradient(90deg,#eef2f4 0%,#dfe6ea 38%,#2f7fc0 40%,#3d8ccb 62%,#e9ecee 64%,#f3f4f5 100%)}
.hero-caption{left:485px;top:258px;width:236px;height:112px;background:rgba(40,44,48,.85);padding:5px 0 0 24px}
.hero-caption li{list-style:none;font-family:"Arimo",Arial,sans-serif;font-size:13px;color:var(--white);line-height:26px;white-space:nowrap}
.hero-arrow{top:255px;width:21px;height:40px;background:#202326;border-radius:3px;display:flex;align-items:center;justify-content:center}

/* sidebar */
.panel{left:36px;width:194px;background:var(--panel-bg);border:1px solid var(--line);border-radius:3px;overflow:hidden}
.panel-title{height:30px;background:linear-gradient(#7890a2,#5f7587);font-family:"Arimo",Arial,sans-serif;font-size:12.5px;color:var(--white);line-height:34px;padding-left:15px;white-space:nowrap}
.panel-foot{position:absolute;left:0;bottom:0;width:100%;height:15px;background:var(--slate-light);font-family:"Arimo",Arial,sans-serif;font-size:9px;color:var(--white);text-align:right;padding-right:22px;line-height:15px}
.panel-text{font-family:"Arimo",Arial,sans-serif;font-size:9px;line-height:13.5px;color:#333}
.nowrap{white-space:nowrap}
.thumb{position:absolute}
.more{color:var(--red-link)}
.link-list{position:absolute;left:86px;top:36px;list-style:none}
.link-list li{font-family:"Arimo",Arial,sans-serif;font-size:9px;line-height:17px;color:#333;white-space:nowrap}
.link-list li::before{content:"›";font-weight:700;margin-right:5px}

/* main copy */
.main{left:265px;top:430px;width:440px}
.main h1{font-family:"Arimo",Arial,sans-serif;font-size:13px;font-weight:400;color:var(--heading);margin-bottom:12px}
.main h1 span{color:var(--accent)}
.main p{font-size:10.5px;line-height:17.4px;color:#444;padding-left:2px}
.highlight{margin:10px 0 14px -1px;width:457px;border:1px solid #b9bdc0;border-radius:4px;background:linear-gradient(#ffffff,#e3e3e3);padding:12px 30px 12px 16px;height:175px}
.highlight p{padding:0}
.highlight ul{list-style:none;margin:8px 0 0 68px}
.highlight li{font-size:10.5px;line-height:21.7px;color:#444;display:flex;align-items:center;gap:7px;white-space:nowrap}
.bullet{width:10px;height:10px;border:1px solid #777;border-radius:50%;display:flex;align-items:center;justify-content:center;flex:none}
.bullet::after{content:"";border-left:4px solid #666;border-top:2.5px solid transparent;border-bottom:2.5px solid transparent;margin-left:1px}
.main .after{padding-left:6px}

/* footer */
.footer{left:0;top:1090px;width:750px;height:110px;background:linear-gradient(var(--slate),var(--slate-dark));color:var(--white);font-family:"Arimo",Arial,sans-serif}
.footer h2{font-weight:400;font-size:13px}
.contact{left:48px;top:12px}
.contact address{font-style:normal;font-size:9px;line-height:15px;margin-top:6px;white-space:nowrap}
.legal{left:264px;top:26px;font-size:9px;white-space:nowrap}
.legal span{margin:0 10px}
.copyright{left:292px;top:50px;font-size:9px;white-space:nowrap}
.connect{left:580px;top:14px}
.social{display:flex;gap:10px;margin:12px 0 0 5px}
.social i{width:18px;height:18px;border-radius:50%;background:#9fb3c2;display:block}
.corner{right:0;bottom:0;width:24px;height:20px;background:#2e3134;color:#fff;font-size:9px;font-family:"Arimo",Arial,sans-serif;text-align:center;line-height:20px}
</style>
</head>
<body>

<header>
  <div class="abs brand"><div class="brand-mark"></div><span class="brand-name">TELOS Consulting</span></div>
  <div class="abs search">
    <svg width="18" height="18" viewBox="0 0 18 18"><circle cx="7" cy="7" r="5" fill="none" stroke="#fff" stroke-width="1.6"/><line x1="11" y1="11" x2="16" y2="16" stroke="#fff" stroke-width="2.2" stroke-linecap="round"/></svg>
  </div>
  <div class="abs phone">
    <span class="phone-icon"><svg width="12" height="14" viewBox="0 0 12 14"><path d="M3 1 L5 4 L3.6 5.5 Q5 9 7.5 10.5 L9 9 L11.5 11.3 L9.5 13 Q3 11 1 3 Z" fill="#fff"/></svg></span>
    +971 4000 5120
  </div>
</header>

<div class="abs nav-band"></div>
<nav class="abs nav">
  <a class="current" href="#">Home</a>
  <a href="#">About TELOS</a>
  <a href="#">Offerings</a>
  <a href="#">Knowledge Base</a>
  <a href="#">Contact Us</a>
</nav>

<div class="abs hero-band"></div>
<div class="abs hero" role="img" aria-label="Photo of three consultants seated at a conference table in front of a partner backdrop"></div>
<ul class="abs hero-caption">
  <li>MANAGING CHANGE</li>
  <li>CULTURE TRANSFORMATION</li>
  <li>EXECUTIVE DEVELOPMENT</li>
  <li>ORGANIZATION SUPPORT</li>
</ul>
<div class="abs hero-arrow" style="left:29px"><svg width="6" height="9"><path d="M5 1 L1.5 4.5 L5 8" fill="none" stroke="#fff" stroke-width="1.4"/></svg></div>
<div class="abs hero-arrow" style="left:700px"><svg width="6" height="9"><path d="M1 1 L4.5 4.5 L1 8" fill="none" stroke="#fff" stroke-width="1.4"/></svg></div>

<aside>
  <section class="abs panel" style="top:422px;height:136px">
    <div class="panel-title">PRESS</div>
    <div class="thumb" role="img" aria-label="Stack of newspapers" style="left:4px;top:42px;width:88px;height:66px;background:linear-gradient(#d8d8d8,#9a9a9a)"></div>
    <p class="abs panel-text nowrap" style="left:99px;top:44px">Lorem ipsum dolor<br>sit amet, consectetuer<br>adipiscing elit. Nam<br>nibh. Nunc varius<br>facilisis eros.</p>
    <div class="panel-foot">Read More</div>
  </section>

  <section class="abs panel" style="top:569px;height:136px">
    <div class="panel-title">PRODUCTS</div>
    <div class="thumb" role="img" aria-label="Illustration of two figures shaking hands" style="left:6px;top:38px;width:64px;height:80px;background:radial-gradient(#5fa0e6,#2a66b8 60%,#f0f2f4 72%)"></div>
    <ul class="link-list">
      <li>Lorem ipsum dolor</li><li>Lorem ipsum dolor</li><li>Lorem ipsum dolor</li><li>Lorem ipsum dolor</li><li>Lorem ipsum dolor</li>
    </ul>
    <div class="panel-foot" style="height:10px"></div>
  </section>

  <section class="abs panel" style="top:716px;height:190px">
    <div class="panel-title">TESTIMONIALS</div>
    <div class="thumb" role="img" aria-label="Client portrait" style="left:10px;top:42px;width:34px;height:40px;background:linear-gradient(#9a8a80,#3a3d42)"></div>
    <p class="abs panel-text nowrap" style="left:54px;top:44px">Lum mlecnean maurilra kerase<br>meras soc totisenonlu sermerse<br>ase lertaslrurbi nuodgravida.<br><span class="more">more</span></p>
    <div class="thumb" role="img" aria-label="Client portrait" style="left:10px;top:108px;width:34px;height:40px;background:linear-gradient(#9a8a80,#3a3d42)"></div>
    <p class="abs panel-text nowrap" style="left:54px;top:109px">Lum mlecnean maurilra kerase<br>meras soc totisenonlu sermerse<br>ase lertaslrurbi nuodgravida.<br><span class="more">more</span></p>
    <div class="panel-foot">Read More</div>
  </section>

  <section class="abs panel" style="top:916px;height:162px">
    <div class="panel-title">RESOURCES AND SERVICES</div>
    <div class="thumb" role="img" aria-label="Hands holding a young plant" style="left:10px;top:38px;width:90px;height:52px;background:linear-gradient(90deg,#d9a58a,#eee8dc 50%,#d9a58a)"></div>
    <p class="abs panel-text nowrap" style="left:106px;top:42px">Lum mlecnean<br>maurilra kerase<br>meras soc totisenonlu</p>
    <p class="abs panel-text nowrap" style="left:15px;top:98px">Lum mlecnean maurilra kerase meras soc<br>totisenonlu sermerse ase lertaslrurbi<br>nuodgravida.</p>
    <div class="panel-foot">Read More</div>
  </section>
</aside>

<main class="abs main">
  <h1>TELOS <span>Consulting</span></h1>
  <p>TELOS Consulting is a firm specialized in providing customized Organization Development solutions to companies in the Middle East and Africa. Recognizing the inability of imported models and solutions to solve problems that face companies in our region, TELOS Consulting builds on international best practices and customizes them to create best-fit solutions that are capable of addressing challenges effectively.</p>
  <p style="margin-top:17px">TELOS Consulting provides Organization Development solutions addressing the "HOW – Soft Side" that is needed to achieve the "WHAT – Business Strategy" in a holistic manner. TELOS Consulting work centers around building an organizational culture that is aligned with and supports the business strategy.</p>
  <div class="highlight">
    <p>TELOS Consulting helps organization develop an aligned humanistic organization design that:</p>
    <ul>
      <li><span class="bullet"></span>Creates a culture of high performance</li>
      <li><span class="bullet"></span>Nurtures leaders &amp; builds human potential</li>
      <li><span class="bullet"></span>Induces innovation across all corporate practices</li>
      <li><span class="bullet"></span>Increases internal organization efficiencies</li>
      <li><span class="bullet"></span>Enhances organization agility</li>
    </ul>
  </div>
  <p class="after">TELOS Consulting utilizes a collaborative consulting model in which consultants work hand in hand with our clients to help them build organizations that support achieving the business strategy. They support clients with the implementation of change initiatives and, most importantly, transfer knowledge and build internal client capability to lead future change programs.</p>
  <p class="after" style="margin-top:17px">At TELOS Consulting, we believe that change can only happen when leadership, people and culture within the organization are open and willing to make this change; therefore in our efforts to implement major changes within the organization, TELOS Consulting uses a culture lens as a major mean to see through the organization and makes its organizational change decisions accordingly.</p>
</main>

<footer class="abs footer">
  <div class="abs contact">
    <h2>CONTACT US</h2>
    <address>Harbor Crescent Road, Palmview Tower,<br>5th Floor, Office # 204<br>P.O. Box 40720, Dubai, UAE<br>Tel: +971 4000 5120</address>
  </div>
  <div class="abs legal">Privacy Policy<span>|</span>Terms &amp; Conditions<span>|</span>Contact Us</div>
  <div class="abs copyright">Copyright © 2012 telos, All Rights Reserved</div>
  <div class="abs connect">
    <h2>CONNECT US</h2>
    <div class="social"><i></i><i></i><i></i><i></i></div>
  </div>
  <div class="abs corner">X2</div>
</footer>

</body>
</html>
```